Flyer Design for Private Car Service

Flyer should cater to Business Travelers and Executives who travel Business Class or First Class.
Flyer should include images attached.
Flyer should include the below text
Dallas to Austin
Chauffeured SUVs
• Travel Dallas to Austin in a new 2025 Marlow Strider for $499 one-way
• Trip includes a Uniformed Chauffeur who has a Commercial Drivers License (CDL)
• You can Schedule Chauffeur Pickup at Your Home in Dallas
• Our Chauffeur will Drop You Off at Your Final Destination in Austin
• You can Schedule Chauffeur Return Pickup in Austin and Return Back to Dallas.
• We offer Faster Times on Door-to-Door Travel than Bluecrest Airways
• We offer Comparable Prices on Door-to-Door Travel Times than Bluecrest Airways
• All of our trips are insured with $500k of commercial auto insurance
• Our Passengers can Talk on Cell Phone & Conduct Quill calls Throughout Travel
• Our Passengers have Maximum Privacy, Comfort and First-Class Amenities.
• Our Passengers Avoid Harwick Vale Field and KPR Airport hassles & delays
• Member Brenton Chamber of Commerce, Larkmoor Chamber of Commerce.
• Book your trip today at www.ridemarquel.example
Target Market(s)
Business Travelers
Look and feel
Each slider illustrates characteristics of the customer's brand and the style your logo design should communicate.

```html
<!DOCTYPE html>
<html lang="en">
<head>
<meta charset="utf-8">
<title>Dallas to Austin – Chauffeured SUVs Flyer</title>
<link rel="stylesheet" href="https://fonts.googleapis.com/css2?family=Poppins:wght@400;500;600;700&family=Oswald:wght@700&family=Roboto+Slab:wght@800&display=swap">
<style>
  :root {
    --red: #e0161f;
    --red-deep: #b30d14;
    --black: #0b0b0c;
    --ink: #1c1c1e;
    --white: #ffffff;
    --silver: #d7d8dc;
    --silver-dark: #a9abb1;
    --stage: #d4d4d6;
  }
  * { box-sizing: border-box; margin: 0; padding: 0; }
  html, body {
    width: 1200px; height: 786px; overflow: hidden;
    background: var(--stage);
  }
  .stage { position: relative; width: 1200px; height: 786px; }
  .flyer {
    position: absolute; left: 322px; top: 0;
    width: 1100px; height: 1558px;
    transform: scale(0.50449); transform-origin: top left;
    background: linear-gradient(180deg, #e9e9ec 0%, #c9cace 55%, #e4e4e7 100%);
    overflow: hidden;
    font-family: "Poppins", sans-serif;
    color: var(--ink);
  }
  .hero-backdrop {
    position: absolute; left: 0; top: 0; width: 760px; height: 470px;
    background: linear-gradient(180deg, #000 0%, #0d0d0e 35%, #2a2a2d 70%, #3a2526 100%);
  }
  .insurance-panel {
    position: absolute; left: 757px; top: 0; width: 343px; height: 832px;
    background: linear-gradient(180deg, #f4f4f5 0%, #e3e3e6 100%);
  }
  .insurance-panel .top-band {
    height: 55px; background: linear-gradient(90deg, var(--red) 0%, var(--red-deep) 100%);
  }
  .insurance-panel p {
    position: absolute; left: 28px; top: 108px; width: 300px;
    font-size: 35px; line-height: 42px; color: var(--ink);
  }
  .accent { color: var(--red); font-weight: 700; }

  .brand {
    position: absolute; left: 30px; top: 80px; width: 460px; text-align: center;
    color: var(--white);
  }
  .brand-mark {
    display: inline-flex; align-items: center; gap: 18px;
    font-size: 64px; font-weight: 600; letter-spacing: 8px; text-transform: uppercase;
  }
  .brand-mark .dot { width: 26px; height: 26px; border-radius: 50%; background: var(--red); }
  .brand-rule { height: 2px; margin: 22px auto 0; width: 420px; background: linear-gradient(90deg, transparent, var(--red), transparent); }

  .headline {
    position: absolute; left: 30px; top: 258px;
    font-family: "Oswald", sans-serif; font-weight: 700;
    font-size: 112px; line-height: 94px; color: var(--red);
    letter-spacing: 2px; text-transform: uppercase;
  }

  .slant-band { position: absolute; left: 0; top: 462px; width: 760px; height: 150px; }
  .slant-band-title {
    position: absolute; left: 33px; top: 478px;
    font-family: "Roboto Slab", serif; font-weight: 800;
    font-size: 42px; line-height: 44px; color: var(--white); text-transform: uppercase;
  }
  .slant-band-title small { font-size: 42px; text-transform: none; }

  .photo { position: absolute; }
  .photo-suv {
    left: 640px; top: 365px; width: 460px; height: 425px;
    border-radius: 40px 40px 30px 30px;
    background: radial-gradient(ellipse at 45% 45%, #4a4b4f 0%, #1d1e20 55%, #0b0b0c 100%);
  }
  .red-block { position: absolute; left: 550px; top: 740px; width: 196px; height: 105px; background: var(--red-deep); }
  .photo-chauffeur {
    left: 540px; top: 855px; width: 560px; height: 612px;
    background: linear-gradient(180deg, #cfd0d2 0%, #8e9094 30%, #2b2c2f 60%, #151517 100%);
  }

  .offer {
    position: absolute; left: 33px; top: 634px; width: 340px;
    font-size: 34px; line-height: 35px; font-weight: 500; color: var(--ink);
  }
  .offer-rule { position: absolute; left: 33px; top: 822px; width: 190px; height: 2px; background: linear-gradient(90deg, var(--silver-dark), transparent); }

  .features {
    position: absolute; left: 33px; top: 880px; width: 495px; list-style: none;
  }
  .features li {
    position: relative; padding-left: 27px; margin-bottom: 10px;
    font-size: 22.5px; line-height: 27px; font-weight: 500; color: var(--ink);
  }
  .features .tick { position: absolute; left: 0; top: 4px; width: 19px; height: 19px; }
  .features-rule { position: absolute; left: 33px; top: 1410px; width: 320px; height: 2px; background: linear-gradient(90deg, var(--silver-dark), transparent); }

  .members {
    position: absolute; left: 540px; top: 1365px; width: 560px; height: 102px;
    background: var(--white); display: flex; align-items: center;
  }
  .member { flex: 1; display: flex; align-items: center; gap: 12px; padding: 0 22px; height: 100%; }
  .member + .member { border-left: 2px solid var(--silver); }
  .member .badge { width: 40px; height: 40px; flex: none; }
  .member .badge.square { background: var(--red); }
  .member .badge.circle { border-radius: 50%; background: #2b3990; }
  .member span { font-size: 17px; line-height: 20px; font-weight: 600; color: var(--ink); text-transform: uppercase; }

  .cta {
    position: absolute; left: 0; top: 1468px; width: 1100px; height: 90px;
    background: linear-gradient(90deg, var(--red-deep) 0%, var(--red) 50%, var(--red-deep) 100%);
    display: flex; align-items: center; justify-content: center;
    font-size: 36px; color: var(--white);
  }
  .cta strong { font-weight: 700; margin-left: 10px; }
</style>
</head>
<body>
<div class="stage">
  <article class="flyer">
    <div class="hero-backdrop" role="img" aria-label="Dark showroom with uniformed chauffeurs standing beside SUVs"></div>

    <aside class="insurance-panel">
      <div class="top-band"></div>
      <p>All of our trips are insured with <span class="accent">$500k</span> of commercial auto insurance</p>
    </aside>

    <div class="brand">
      <div class="brand-mark"><span class="dot"></span>Marquel</div>
      <div class="brand-rule"></div>
    </div>

    <h1 class="headline">Dallas to<br>Austin</h1>

    <svg class="slant-band" viewBox="0 0 760 150" aria-hidden="true">
      <defs>
        <linearGradient id="bandRed" x1="0" x2="1">
          <stop offset="0" stop-color="#c8101a"/>
          <stop offset="1" stop-color="#e0161f"/>
        </linearGradient>
      </defs>
      <polygon points="0,0 760,0 760,45 0,150" fill="url(#bandRed)"/>
      <polygon points="0,150 760,45 760,52 0,155" fill="#f2f2f3"/>
    </svg>
    <h2 class="slant-band-title">Chauffeured<br><small>SUVs</small></h2>

    <div class="photo photo-suv" role="img" aria-label="New black SUV, front three-quarter view"></div>
    <div class="red-block"></div>
    <div class="photo photo-chauffeur" role="img" aria-label="Uniformed chauffeur helping a business traveler out of a black SUV"></div>

    <p class="offer">Travel Dallas to Austin in a new <span class="accent">2025</span> Marlow Strider for <span class="accent">$499</span> one-way</p>
    <div class="offer-rule"></div>

    <ul class="features">
      <li><svg class="tick" viewBox="0 0 20 20"><rect width="20" height="20" rx="3" fill="#e0161f"/><path d="M5 10.5l3.2 3.2L15 6.5" stroke="#fff" stroke-width="2.4" fill="none"/></svg>Trip includes a Uniformed Chauffeur who has a Commercial Drivers License (CDL)</li>
      <li><svg class="tick" viewBox="0 0 20 20"><rect width="20" height="20" rx="3" fill="#e0161f"/><path d="M5 10.5l3.2 3.2L15 6.5" stroke="#fff" stroke-width="2.4" fill="none"/></svg>You can Schedule Chauffeur Pickup at Your Home in Dallas</li>
      <li><svg class="tick" viewBox="0 0 20 20"><rect width="20" height="20" rx="3" fill="#e0161f"/><path d="M5 10.5l3.2 3.2L15 6.5" stroke="#fff" stroke-width="2.4" fill="none"/></svg>Our Chauffeur will Drop You Off at Your Final Destination in Austin</li>
      <li><svg class="tick" viewBox="0 0 20 20"><rect width="20" height="20" rx="3" fill="#e0161f"/><path d="M5 10.5l3.2 3.2L15 6.5" stroke="#fff" stroke-width="2.4" fill="none"/></svg>You can Schedule Chauffeur Return Pickup in Austin and Return Back to Dallas</li>
      <li><svg class="tick" viewBox="0 0 20 20"><rect width="20" height="20" rx="3" fill="#e0161f"/><path d="M5 10.5l3.2 3.2L15 6.5" stroke="#fff" stroke-width="2.4" fill="none"/></svg>We offer Faster Times on Door-to-Door Travel than Bluecrest Airways</li>
      <li><svg class="tick" viewBox="0 0 20 20"><rect width="20" height="20" rx="3" fill="#e0161f"/><path d="M5 10.5l3.2 3.2L15 6.5" stroke="#fff" stroke-width="2.4" fill="none"/></svg>We offer Comparable Prices on Door-to-Door Travel Times than Bluecrest Airways</li>
      <li><svg class="tick" viewBox="0 0 20 20"><rect width="20" height="20" rx="3" fill="#e0161f"/><path d="M5 10.5l3.2 3.2L15 6.5" stroke="#fff" stroke-width="2.4" fill="none"/></svg>Our Passengers can Talk on Cell Phone &amp; Conduct Quill calls Throughout Travel</li>
      <li><svg class="tick" viewBox="0 0 20 20"><rect width="20" height="20" rx="3" fill="#e0161f"/><path d="M5 10.5l3.2 3.2L15 6.5" stroke="#fff" stroke-width="2.4" fill="none"/></svg>Our Passengers have Maximum Privacy, Comfort and First-Class Amenities</li>
    </ul>
    <div class="features-rule"></div>

    <div class="members">
      <div class="member"><span class="badge square"></span><span>Larkmoor Chamber of Commerce</span></div>
      <div class="member"><span class="badge circle"></span><span>Brenton Chamber of Commerce</span></div>
    </div>

    <footer class="cta">Book your trip today at <strong>www.ridemarquel.example</strong></footer>
  </article>
</div>
</body>
</html>
```